Postcard design for Intellectual Property Professional Conference

Seeking design for 5.5" by 8.5" postcard mailer about a conference on tax and finance issues for international IP management. Attendees are lawyers and financial executives. Draft language is attached.

Target Market(s)

The project should have the attached picture of Boston with the caption "Courtesy of the Harborline Meeting & Travelers Council"

Industry/Entity Type

Finance

```html
<!DOCTYPE html>
<html lang="en">
<head>
<meta charset="utf-8">
<title>Intellectual Property in Developing Growth Markets — Conference Postcard</title>
<link rel="stylesheet" href="https://fonts.googleapis.com/css2?family=Bebas+Neue&family=Source+Sans+3:wght@400;600;700&display=swap">
<style>
  :root{
    --navy-deep:#050b16;
    --navy:#0b1a30;
    --steel:#1d3f66;
    --glow:#3f8fd0;
    --accent:#2b9be6;
    --heading-blue:#1a8ad4;
    --white:#ffffff;
    --panel:#ffffff;
    --ink:#2a2a2a;
    --caption:#b9c9dc;
  }
  html,body{margin:0;padding:0;overflow:hidden;background:var(--white);}
  .postcard{
    position:relative;width:1200px;height:776px;overflow:hidden;
    font-family:"Source Sans 3",Arial,sans-serif;
  }
  .hero{
    position:absolute;left:0;top:0;width:872px;height:776px;
    background:
      radial-gradient(ellipse 420px 320px at 560px 300px, rgba(63,143,208,.55), rgba(63,143,208,0) 70%),
      radial-gradient(ellipse 300px 260px at 700px 120px, rgba(120,170,210,.35), rgba(0,0,0,0) 70%),
      linear-gradient(180deg, var(--navy) 0%, var(--navy-deep) 100%);
  }
  .site-url{
    position:absolute;left:49px;top:28px;margin:0;
    color:var(--white);font-size:17px;font-weight:400;letter-spacing:.2px;
  }
  .city-photo{
    position:absolute;left:636px;top:26px;width:212px;height:132px;margin:0;
  }
  .city-photo-image{
    width:212px;height:118px;
    background:linear-gradient(180deg,#6f9cc6 0%,#3d6a96 55%,#1c3552 100%);
    border:1px solid rgba(255,255,255,.6);
    box-sizing:border-box;
  }
  .city-photo figcaption{
    margin-top:3px;color:var(--caption);font-size:9.5px;line-height:11px;font-style:italic;
  }
  .title{
    position:absolute;left:43px;top:186px;margin:0;
    font-family:"Bebas Neue",Impact,sans-serif;font-weight:400;
    font-size:58px;line-height:53px;color:var(--white);
    text-shadow:4px 4px 0 rgba(0,0,0,.55);
  }
  .title .highlight{color:var(--accent);display:block;}
  .title .line{display:block;}
  .divider{
    position:absolute;left:43px;top:421px;width:328px;height:2px;background:var(--white);
  }
  .event-when{
    position:absolute;left:45px;top:448px;margin:0;
    font-family:"Bebas Neue",Impact,sans-serif;font-size:27px;line-height:27px;
    color:var(--white);
  }
  .intro{
    position:absolute;left:43px;top:539px;width:800px;margin:0;
    color:var(--white);font-size:17.6px;line-height:20px;
  }
  .intro p{margin:0 0 20px;}
  .topics{
    position:absolute;left:872px;top:0;width:328px;height:776px;background:var(--panel);
  }
  .topics-heading{
    position:absolute;left:22px;top:28px;margin:0;
    color:var(--heading-blue);font-size:19px;font-weight:700;
  }
  .topic-list{
    position:absolute;left:24px;top:54px;width:287px;margin:0;padding:0;list-style:none;
    color:var(--ink);font-size:16.4px;line-height:19.6px;
  }
  .topic-list li{position:relative;padding-left:17px;margin-bottom:7px;}
  .topic-list li::before{
    content:"";position:absolute;left:2px;top:5px;
    border-left:8px solid var(--heading-blue);
    border-top:5px solid transparent;border-bottom:5px solid transparent;
  }
  .register{
    position:absolute;left:38px;top:684px;margin:0;
    font-family:"Bebas Neue",Impact,sans-serif;font-size:37px;line-height:37px;
    color:var(--heading-blue);
  }
</style>
</head>
<body>
<div class="postcard">
  <div class="hero" role="img" aria-label="Businessman in a suit drawing a glowing business growth chart with a world map, rising arrow and strategy keywords on a dark blue screen"></div>

  <p class="site-url">www.meridianforesight.com</p>

  <figure class="city-photo">
    <div class="city-photo-image" role="img" aria-label="Photograph of the Boston skyline across the harbor"></div>
    <figcaption>Courtesy of the Harborline Meeting &amp; Travelers Council</figcaption>
  </figure>

  <h1 class="title">
    <span class="line">Intellectual</span>
    <span class="line">Property in</span>
    <span class="highlight">Developing</span>
    <span class="highlight">Growth Markets</span>
  </h1>

  <div class="divider"></div>

  <p class="event-when">Boston<br>March 24 &amp; 25, 2016</p>

  <div class="intro">
    <p>You are cordially invited to attend a comprehensive and practical day and a half conference to examine the tax and legal structuring strategies for increasing profits from Intellectual properties while protecting these important assets when doing business in fast growing developing markets. Intellectual property assets include some of the most important assets of most companies: their patents, trade marks, copyrights, brand names and licensing agreements.</p>
    <p>Senior tax, legal and financial experts will provide a comprehensive analysis of the legal issues, recent tax &amp; regulatory developments, skills and structuring strategies necessary to maximize profits from IP Migrating IP assets to low tax jurisdiction will also be covered along with dealing with issues of piracy, counterfeiting, infringement and other legal challenges to a company’s IP.</p>
  </div>

  <aside class="topics">
    <h2 class="topics-heading">Topics to be covered include:</h2>
    <ul class="topic-list">
      <li>Market trends in IP tax &amp; legal structures</li>
      <li>Proposed US Tax changes and regulatory developments outside the US including European and OECD developments affecting IP, patent box, base erosion and profit splitting (BEPS)</li>
      <li>Overview of the IP landscape in key developing growth markets such as China, India, Brazil, Korea, South Africa, Mexico and other developing markets outside the US.</li>
      <li>Legal issues including litigation, arbitration and use of government assistance to protect IP values in key developing markets.</li>
      <li>Monetizing IP assets and rights in regard to divestitures, spin offs, split offs, M&amp;A, transfers of ownership and securitizations in developing growth markets</li>
      <li>Special Tax Planning and Legal Considerations for IP in Particular Sectors such as Biopharmaceutical, International Sports Licensing, High Tech, Consumer Brands, and Manufacuring</li>
      <li>Restructuring and Migration of IP Assets to Tax Advantaged Jurisdictions</li>
    </ul>
    <p class="register">Register Early<br>and Save up to $300</p>
  </aside>
</div>
</body>
</html>
```